Brindle Logistics Business Card Design

We are a trucking and warehousing company. We run freight in the US manly from the Pacific NW to TX and back up the the PNW. We also do warehousing where we store, move, and distribute freight. Looking for a clean and modern design of business card. We would like to look rich and elegant. Attached is our logo.

Industry/Entity Type

Trucking Company

Contact Information for Business Card

Looking for a clean and modern design of business card. We would like to look rich and elegant.

Font styles to use
Sans Serif

Colors

Designer to choose colors to be used in the design.

Requirements
Must have
• logo but it should not dominate the card
Should not have
• logo should not dominate the card

```html
<!DOCTYPE html>
<html lang="en">
<head>
<meta charset="utf-8">
<title>Brindle Logistics Business Card</title>
<link href="https://fonts.googleapis.com/css2?family=Montserrat:wght@500;600;700&display=swap" rel="stylesheet">
<style>
  :root {
    --backdrop: #5e5e5e;
    --card: #4a4a4a;
    --card-deep: #3a3a3a;
    --tread: #2f2f2f;
    --band: #414141;
    --ink: #ffffff;
    --name: #e6e6e6;
    --accent: #f2c200;
    --icon-bg: #0b63d1;
  }
  * { margin: 0; padding: 0; box-sizing: border-box; }
  html, body { width: 1200px; height: 1193px; overflow: hidden; }
  body {
    background: var(--backdrop);
    font-family: "Montserrat", sans-serif;
    position: relative;
  }
  .card {
    position: absolute;
    width: 788px;
    height: 471px;
    background: var(--card);
    overflow: hidden;
  }
  .card--front { left: 193px; top: 88px; }
  .card--back { left: 195px; top: 591px; }
  .card svg.decor { position: absolute; left: 0; top: 0; }
  .holder {
    position: absolute;
    left: 289px;
    top: 108px;
    white-space: nowrap;
  }
  .holder__name {
    font-weight: 700;
    font-size: 41px;
    color: var(--name);
    letter-spacing: 0.5px;
  }
  .holder__role {
    font-weight: 700;
    font-size: 23px;
    color: var(--accent);
    margin-left: 6px;
  }
  .contact {
    position: absolute;
    display: flex;
    align-items: center;
    gap: 14px;
    color: var(--ink);
    font-weight: 500;
    font-size: 19px;
    white-space: nowrap;
  }
  .contact__icon {
    width: 28px; height: 28px;
    background: var(--icon-bg);
    display: flex; align-items: center; justify-content: center;
  }
  .contact--address { right: 354px; top: 289px; }
  .contact--phone { right: 354px; top: 333px; }
  .contact--email { right: 71px; top: 288px; }
  .contact--web { right: 71px; top: 332px; }
  .brand {
    position: absolute;
    left: 185px;
    top: 190px;
    display: flex;
    align-items: center;
    gap: 24px;
    color: var(--ink);
  }
  .brand__mark {
    width: 96px; height: 96px;
    border-radius: 50%;
    background: var(--ink);
  }
  .brand__name {
    font-weight: 600;
    line-height: 1;
    text-transform: uppercase;
  }
  .brand__name span { display: block; }
  .brand__name .brand__main { font-size: 58px; letter-spacing: 2px; }
  .brand__name .brand__sub { font-size: 30px; letter-spacing: 1.5px; margin-top: 8px; }
</style>
</head>
<body>

<section class="card card--front">
  <svg class="decor" width="788" height="471" viewBox="0 0 788 471">
    <defs>
      <linearGradient id="treadFront" x1="0" y1="0" x2="1" y2="1">
        <stop offset="0" stop-color="#333"/>
        <stop offset="1" stop-color="#3c3c3c"/>
      </linearGradient>
    </defs>
    <polygon role="img" aria-label="Tyre track decoration" fill="url(#treadFront)" points="130,0 305,0 75,471 0,471 0,260"/>
    <g class="stripe-band" fill="var(--tread)">
      <polygon points="245,171 290,171 255,243 210,243"/>
      <polygon points="307,171 352,171 317,243 272,243"/>
      <polygon points="369,171 414,171 379,243 334,243"/>
      <polygon points="431,171 476,171 441,243 396,243"/>
      <polygon points="493,171 538,171 503,243 458,243"/>
      <polygon points="555,171 600,171 565,243 520,243"/>
      <polygon points="617,171 662,171 627,243 582,243"/>
      <polygon points="679,171 724,171 689,243 644,243"/>
      <polygon points="741,171 786,171 751,243 706,243"/>
      <polygon points="803,171 788,171 788,200"/>
    </g>
    <g class="stripe-band" fill="var(--tread)">
      <polygon points="140,395 185,395 148,471 103,471"/>
      <polygon points="202,395 247,395 210,471 165,471"/>
      <polygon points="264,395 309,395 272,471 227,471"/>
      <polygon points="326,395 371,395 334,471 289,471"/>
      <polygon points="388,395 433,395 396,471 351,471"/>
      <polygon points="450,395 495,395 458,471 413,471"/>
      <polygon points="512,395 557,395 520,471 475,471"/>
      <polygon points="574,395 619,395 582,471 537,471"/>
      <polygon points="636,395 681,395 644,471 599,471"/>
      <polygon points="698,395 743,395 706,471 661,471"/>
      <polygon points="760,395 788,395 788,420 768,471 723,471"/>
    </g>
  </svg>

  <div class="holder">
    <span class="holder__name">OWEN MARSH</span><span class="holder__role">MANAGER</span>
  </div>

  <div class="contact contact--address">
    <span>Leeds,Str.Carter 9</span>
    <span class="contact__icon"><svg width="16" height="16" viewBox="0 0 16 16"><path d="M8 2 1.5 8H3.5V14H6.5V10H9.5V14H12.5V8H14.5Z" fill="#fff"/></svg></span>
  </div>
  <div class="contact contact--phone">
    <span>008 412 730 5196</span>
    <span class="contact__icon"><svg width="16" height="16" viewBox="0 0 16 16"><path d="M4 1.5 6.2 4.3 4.9 6c.9 2 2.4 3.6 4.3 4.6l1.6-1.3 2.8 2.2-1.3 2.1C7 13.4 2.6 8.9 2 3Z" fill="#fff"/></svg></span>
  </div>
  <div class="contact contact--email">
    <span>hello@mailbox.com</span>
    <span class="contact__icon"><svg width="16" height="16" viewBox="0 0 16 16"><rect x="1.5" y="3.5" width="13" height="9" fill="#fff"/><path d="M1.5 3.5 8 9 14.5 3.5" fill="none" stroke="#0b63d1" stroke-width="1.2"/></svg></span>
  </div>
  <div class="contact contact--web">
    <span>www.sitename.com</span>
    <span class="contact__icon"><svg width="16" height="16" viewBox="0 0 16 16" fill="none" stroke="#fff" stroke-width="1.2"><circle cx="8" cy="8" r="6.2"/><ellipse cx="8" cy="8" rx="2.7" ry="6.2"/><path d="M1.8 8H14.2M2.8 5H13.2M2.8 11H13.2"/></svg></span>
  </div>
</section>

<section class="card card--back">
  <svg class="decor" width="788" height="472" viewBox="0 0 788 472">
    <defs>
      <linearGradient id="treadBack" x1="0" y1="0" x2="1" y2="1">
        <stop offset="0" stop-color="#313131"/>
        <stop offset="1" stop-color="#363636"/>
      </linearGradient>
    </defs>
    <polygon role="img" aria-label="Tyre track decoration" fill="url(#treadBack)" points="0,0 477,0 788,380 788,472 316,472 0,90"/>
    <rect class="logo-band" x="0" y="182" width="788" height="122" fill="var(--band)" opacity="0.45"/>
  </svg>

  <div class="brand">
    <div class="brand__mark"></div>
    <div class="brand__name">
      <span class="brand__main">Brindle</span>
      <span class="brand__sub">Logistics, LLC</span>
    </div>
  </div>
</section>

</body>
</html>
```